Clearview Property Inspections

Property Inspection ( pre-purchase building inspections, swimming pool inspection, pest inspection , maintenance)

Industry/Entity Type

Building

Contact Information for Business Card

Tomas Varnell
info@clearviewinspect-demo.com.au
0412 867 219

ClearView Property Inspections
www.clearviewinspect-demo.com.au

on the back

Property Inspections
Property Maintenance

Safe Home....Safe Familu

```html
<!DOCTYPE html>
<html lang="en">
<head>
<meta charset="utf-8">
<title>Clearview Property Inspections – Business Card</title>
<link rel="stylesheet" href="https://fonts.googleapis.com/css2?family=Hind:wght@400;700&display=swap">
<style>
  :root {
    --backdrop: #000000;
    --card: #ffffff;
    --brand-blue: #2a52a0;
    --ink: #1e1e1e;
    --on-blue: #ffffff;
  }
  html, body {
    margin: 0;
    padding: 0;
    width: 1200px;
    height: 1000px;
    overflow: hidden;
    background: var(--backdrop);
    font-family: "Hind", "Frutiger", Arial, sans-serif;
  }
  .canvas {
    position: relative;
    width: 1200px;
    height: 1000px;
  }
  .card {
    position: absolute;
    left: 33px;
    top: 152px;
    width: 1133px;
    height: 685px;
    background: var(--card);
  }
  .brand-block {
    position: absolute;
    left: 111px;
    top: -2px;
    width: 387px;
    height: 332px;
    background: var(--brand-blue);
    display: flex;
    align-items: center;
    justify-content: center;
  }
  .brand-name {
    margin: 0;
    color: var(--on-blue);
    font-weight: 700;
    font-size: 34px;
    line-height: 1.15;
    text-align: center;
    letter-spacing: 0.5px;
  }
  .accent-bar {
    position: absolute;
    left: 111px;
    bottom: 0;
    width: 387px;
    height: 42px;
    background: var(--brand-blue);
  }
  .holder-name {
    position: absolute;
    right: 635px;
    top: 474px;
    margin: 0;
    color: var(--brand-blue);
    font-weight: 700;
    font-size: 37px;
    line-height: 1;
    white-space: nowrap;
  }
  .contact-list {
    position: absolute;
    left: 558px;
    top: 474px;
    margin: 0;
    padding: 0;
    list-style: none;
    font-size: 32px;
    line-height: 40px;
    color: var(--ink);
  }
  .contact-list .company {
    color: var(--brand-blue);
    font-weight: 700;
  }
</style>
</head>
<body>
  <main class="canvas">
    <section class="card">
      <div class="brand-block">
        <p class="brand-name">Clearview<br>Property Inspections</p>
      </div>
      <div class="accent-bar"></div>
      <h1 class="holder-name">Tomas Varnell</h1>
      <ul class="contact-list">
        <li class="email">info@clearviewinspect-demo.com.au</li>
        <li class="phone">0412 867 219</li>
        <li class="company">ClearView Property Inspections</li>
        <li class="website">www.clearviewinspect-demo.com.au</li>
      </ul>
    </section>
  </main>
</body>
</html>
```